Business Card Design - Brightfold Dwellings

Hi there,

We would like a business card for our new venture, Brightfold Dwellings.

We are based in Western Australia and specialise in taking tired, old properties and making them look new again. We aim to create enjoyably liveable homes for young families in particular.

Product pricing is mid range i.e. appliances, furnishings, fixtures (not top end but not cheap either)

Our work is primarily cosmetic renovation (approx. 80%) and the rest construction (approx 20%).

We would like a business card that conveys the following:
- clean, simplistic/minimalistic design
- modern, contemporary style
- a touch of funk/uniqueness
- appealing to both females and males
- professionalism

I have uploaded our logo in grey or green, I do not mind which one you choose to use (please use either coloured logo on the pure white background not the white on colour version).

Details to include on the business card are:
Names: Corina Maddox and Pete Okonbrie
Mobile: 0417 362 908
Email: info@brightfolddwellings.com.au
Website: www.brightfolddwellings.com.au (note: this website is currently being developed)
Note: We will provide final details such as mobile number and names on on selection of successful design)

On the other side of the card please include a line similar to "We find worn, dated houses and hand them back fresh and bright!"

The business card will also need to include the following "ABN 47 219 635 104" which is our Australian Business Number (again the actual number will be provided on selection of successful design). We would like this number somewhere near our name Brightfold Dwellings but in much smaller text.

The purpose of the business cards will be to give to suppliers, real estate agents, people wanting assistance in locating a property in need of renovation and potential buyers.

Thank you and please let me know if you have any further questions.

```html
<!DOCTYPE html>
<html lang="en">
<head>
<meta charset="utf-8">
<title>Brightfold Dwellings – Business Card</title>
<link rel="stylesheet" href="https://fonts.googleapis.com/css2?family=Questrial&family=Arimo:ital,wght@0,400;0,700;1,400;1,700&display=swap">
<style>
  :root {
    --page: #e9e7e3;
    --card-white: #ffffff;
    --charcoal-dark: #2e2f31;
    --charcoal-light: #55575a;
    --lime: #a9c51e;
    --ink-light: #f2f2f2;
    --ink-grey: #6d6e70;
  }
  * { margin: 0; padding: 0; box-sizing: border-box; }
  html, body {
    width: 1200px; height: 1023px; overflow: hidden;
    background: var(--page);
    font-family: "Arimo", Arial, sans-serif;
  }
  .card {
    position: absolute; left: 222px;
    width: 756px; height: 460px;
    overflow: hidden;
    box-shadow: 0 6px 18px rgba(0,0,0,.18);
  }
  .card--front { top: 36px; background: var(--card-white); }
  .card--back {
    top: 527px;
    background: linear-gradient(160deg, var(--charcoal-light) 0%, var(--charcoal-dark) 75%);
  }
  .front-shape { position: absolute; inset: 0; }
  .brand-name {
    position: absolute;
    font-family: "Questrial", "Century Gothic", sans-serif;
    color: var(--lime);
    white-space: nowrap;
    letter-spacing: -0.5px;
  }
  .card--front .brand-name { left: 96px; top: 130px; font-size: 54px; }
  .abn {
    position: absolute; right: 30px; top: 22px;
    font-size: 15px; color: var(--lime); letter-spacing: .5px;
  }
  .person { position: absolute; left: 44px; top: 348px; color: var(--lime); }
  .person__name { font-weight: 700; font-size: 31px; letter-spacing: .5px; }
  .person__role { font-size: 25px; margin-top: 2px; }
  .contacts {
    position: absolute; left: 462px; top: 292px;
    list-style: none; color: var(--ink-light); font-size: 16px;
  }
  .contacts li { display: flex; align-items: center; gap: 8px; height: 27px; }
  .contacts svg { width: 16px; height: 16px; flex: none; }
  .card--back .brand-name { right: 70px; top: 120px; font-size: 60px; }
  .tagline {
    position: absolute; right: 70px; top: 208px; width: 430px;
    text-align: center; color: var(--ink-light);
    font-style: italic; font-size: 19px; line-height: 1.3;
  }
  .back-web {
    position: absolute; left: 44px; bottom: 34px;
    color: var(--lime); font-weight: 700; font-style: italic; font-size: 20px; letter-spacing: .5px;
  }
</style>
</head>
<body>

<section class="card card--front">
  <svg class="front-shape" viewBox="0 0 756 460" preserveAspectRatio="none" aria-hidden="true">
    <defs>
      <linearGradient id="charcoal" x1="0" y1="0" x2="0.3" y2="1">
        <stop offset="0" stop-color="#55575a"/>
        <stop offset="1" stop-color="#2e2f31"/>
      </linearGradient>
    </defs>
    <path d="M0,318 C210,300 420,300 560,250 C650,218 710,190 756,170 L756,460 L0,460 Z" fill="url(#charcoal)"/>
    <path d="M0,300 C210,282 420,282 560,232 C650,200 710,172 756,152" fill="none" stroke="#a9c51e" stroke-width="2"/>
  </svg>
  <p class="abn">ABN 47 219 635 104</p>
  <p class="brand-name">Brightfold Dwellings</p>
  <div class="person">
    <p class="person__name">CORINA MADDOX</p>
    <p class="person__role">Director</p>
  </div>
  <ul class="contacts">
    <li>
      <svg viewBox="0 0 16 16"><rect width="16" height="16" rx="2" fill="#a9c51e"/><rect x="5" y="2.5" width="6" height="11" rx="1" fill="#2e2f31"/></svg>
      0417 362 908
    </li>
    <li>
      <svg viewBox="0 0 16 16"><rect width="16" height="16" rx="2" fill="#a9c51e"/><rect x="3" y="4.5" width="10" height="7" fill="#2e2f31"/><path d="M3,4.5 L8,8.5 L13,4.5" fill="none" stroke="#a9c51e" stroke-width="1"/></svg>
      info@brightfolddwellings.com.au
    </li>
    <li>
      <svg viewBox="0 0 16 16"><rect width="16" height="16" rx="2" fill="#a9c51e"/><circle cx="8" cy="8" r="5" fill="none" stroke="#2e2f31" stroke-width="1.3"/><path d="M3,8 H13 M8,3 V13" stroke="#2e2f31" stroke-width="1"/></svg>
      www.brightfolddwellings.com.au
    </li>
  </ul>
</section>

<section class="card card--back">
  <p class="brand-name">Brightfold Dwellings</p>
  <p class="tagline">"We find worn, dated houses<br>and<br>hand them back fresh and bright!"</p>
  <p class="back-web">www.brightfolddwellings.com.au</p>
</section>

</body>
</html>
```